Business card design needed

We do excavation, cartage and contracting
I would quote like to have a picture of my digger as the whole back ground and the words on top. If that looks any good
Otherwise please feel free to come up with any other cool options

Cheers Marc

KLR Contracting
Excavation, Cartage, Contracting
Marcus Prewitt
www.klr-example.co.nz
021 584 067
marc@klr-example.co.nz

```html
<!DOCTYPE html>
<html lang="en">
<head>
<meta charset="utf-8">
<title>KLR Contracting – Business Card</title>
<link href="https://fonts.googleapis.com/css2?family=Arimo:wght@400;700&display=swap" rel="stylesheet">
<style>
  :root {
    --backdrop: #9a9c9e;
    --card-black: #0b0b0b;
    --brand-yellow: #f5d90a;
    --gold: #e3c21a;
    --ink: #111111;
    --photo-dark: #141414;
    --photo-mid: #4a4740;
    --photo-yellow: #b99a1c;
  }
  * { margin: 0; padding: 0; box-sizing: border-box; }
  html, body {
    width: 1200px; height: 848px; overflow: hidden;
    background: var(--backdrop);
    font-family: "Arimo", Arial, sans-serif;
  }
  .canvas { position: relative; width: 1200px; height: 848px; }

  .card {
    position: absolute; width: 350px; height: 197px; overflow: hidden;
  }
  .card-front { left: 319px; top: 199px; background: var(--card-black); }
  .card-back { left: 537px; top: 441px; }

  .front-top {
    height: 122px; display: flex; flex-direction: column;
    align-items: center; justify-content: center; gap: 10px;
  }
  .brand-name {
    color: var(--gold); font-weight: 700; font-size: 34px; letter-spacing: 2px;
    line-height: 1;
  }
  .tagline { color: var(--brand-yellow); font-size: 10.5px; }

  .front-band {
    height: 75px; background: var(--brand-yellow);
    display: flex; align-items: center;
  }
  .holder-name {
    width: 208px; padding-left: 34px;
    font-weight: 700; font-size: 17px; color: var(--ink);
  }
  .contact {
    border-left: 2px solid var(--ink); padding-left: 7px;
    font-size: 9.5px; line-height: 1.45; color: var(--ink);
  }
  .contact b { font-weight: 700; }

  .back-photo {
    position: absolute; inset: 0;
    background:
      radial-gradient(ellipse at 55% 40%, var(--photo-yellow) 0%, rgba(185,154,28,0) 40%),
      radial-gradient(ellipse at 40% 75%, var(--photo-mid) 0%, rgba(74,71,64,0) 60%),
      var(--photo-dark);
  }
  .back-mark {
    position: absolute; inset: 0; display: flex; align-items: center; justify-content: center;
    color: rgba(255,255,255,0.35); font-weight: 700; font-size: 70px; letter-spacing: 4px;
  }
</style>
</head>
<body>
<div class="canvas">
  <section class="card card-front">
    <div class="front-top">
      <div class="brand-name">KLR</div>
      <div class="tagline">Contracting Excavation • Cartage</div>
    </div>
    <div class="front-band">
      <div class="holder-name">Marcus Prewitt</div>
      <div class="contact">
        <div><b>t:</b> 021 584 067</div>
        <div><b>e:</b> marc@klr-example.co.nz</div>
        <div><b>www.klr-example.co.nz</b></div>
      </div>
    </div>
  </section>

  <section class="card card-back">
    <div class="back-photo" role="img" aria-label="Photo of a yellow digger bucket working in dark earth"></div>
    <div class="back-mark">KLR</div>
  </section>
</div>
</body>
</html>
```